Visitenkarten für Urologisches Zentrum Lindenhof
Zielgruppe
Urologisches Zentrum Lindenhof / Vasektomie-Zentrum Lindenhof
Aufgabenstellung
Bitte an der alten Vorlage orientieren. Die 1. Seite (Aussenseite der Klappkarte) ist in Ordnung.
2. Seite (Innenseite der Klappkarte): Hier ggf. eine besser lesbare Schrift.
Adresse: Dr. med. FELIX BRANDT &
Dr. med. MARTIN OSWALD
Birkenweg 17
68161 Mannheim
Fon: unverändert, jedoch bitte etwas übersichtlicher
Fax: unverändert, jedoch bitte etwas übersichtlicher
E-Mail: unverändert, jedoch bitte etwas übersichtlicher
Web: unverändert, jedoch bitte etwas übersichtlicher
Öffnungszeiten: Mo,Di: 08:00 - 12:00 Uhr
14:00 - 16:00 Uhr
Mi: 08:00 - 12:00 Uhr
Do,Fr: 08.00 - 12:00 Uhr
Es sollte noch folgender Text eingefügt werden: Wußten Sie schon? Sie können bei uns Termine über www.terminofix.de
vereinbaren.
Bitte machen Sie uns einige dynamischere Gestaltungsvorschläge. Die Karte sollte in weiß gehalten werden. Keine Glanzbeschichtung und etwas kräftigeres, hochwertiges Papier.
Ich freue mich auf Ihre Vorschläge.

```html
<!DOCTYPE html>
<html lang="de">
<head>
<meta charset="utf-8">
<title>Visitenkarte – Urologisches Zentrum Lindenhof</title>
<link rel="stylesheet" href="https://fonts.googleapis.com/css2?family=Fira+Sans:wght@400;500;600&display=swap">
<style>
  :root {
    --green: #8bb028;
    --green-dark: #6f8f1c;
    --ink: #3a3f33;
    --muted: #7b8070;
    --white: #ffffff;
    --fold: #d9ddd0;
  }
  * { margin: 0; padding: 0; box-sizing: border-box; }
  html, body { width: 1200px; height: 388px; overflow: hidden; background: var(--white); }
  body { font-family: "Fira Sans", Arial, sans-serif; color: var(--ink); }

  .card { position: relative; width: 1200px; height: 388px; background: var(--white); }
  .panel { position: absolute; top: 0; width: 600px; height: 388px; overflow: hidden; }
  .panel--contact { left: 0; }
  .panel--hours { left: 600px; border-left: 1px dashed var(--fold); }
  .accent { position: absolute; inset: 0; width: 600px; height: 388px; }

  /* contact side */
  .doctors { position: absolute; left: 56px; top: 38px; }
  .doctors__name { font-size: 25px; font-weight: 600; color: var(--green); line-height: 32px; }
  .doctors__title { font-weight: 400; color: var(--muted); }

  .address { position: absolute; left: 56px; top: 138px; font-size: 17px; line-height: 25px; }

  .contacts { position: absolute; left: 56px; top: 212px; display: grid;
    grid-template-columns: 64px auto; row-gap: 6px; column-gap: 10px; font-size: 17px; line-height: 22px; }
  .label { font-size: 12px; font-weight: 600; letter-spacing: .08em; text-transform: uppercase;
    color: var(--green); line-height: 22px; }

  /* hours side */
  .hours-title { position: absolute; left: 56px; top: 38px; font-size: 27px; font-weight: 600; color: var(--green); }
  .hours { position: absolute; left: 56px; top: 94px; border-collapse: collapse; font-size: 17px; }
  .hours th { text-align: left; font-weight: 600; color: var(--green-dark); width: 86px; vertical-align: top; padding: 5px 0; }
  .hours td { padding: 5px 0; line-height: 24px; }
  .hours tr + tr { border-top: 1px solid #e7eadf; }

  .notice { position: absolute; left: 56px; top: 290px; padding-left: 12px;
    border-left: 3px solid var(--green); font-size: 12.5px; line-height: 17px; color: var(--muted); }
  .notice strong { color: var(--ink); font-weight: 600; }
</style>
</head>
<body>
<div class="card">
  <section class="panel panel--contact">
    <svg class="accent" viewBox="0 0 600 388" aria-hidden="true">
      <polygon points="420,388 600,250 600,388" fill="var(--green)"/>
      <polygon points="500,388 600,312 600,388" fill="var(--green-dark)"/>
      <rect x="56" y="112" width="60" height="4" fill="var(--green)"/>
    </svg>
    <div class="doctors">
      <div class="doctors__name"><span class="doctors__title">Dr. med.</span> Felix Brandt</div>
      <div class="doctors__name"><span class="doctors__title">Dr. med.</span> Martin Oswald</div>
    </div>
    <div class="address">Birkenweg 17<br>68161 Mannheim</div>
    <div class="contacts">
      <span class="label">Fon</span><span>0621 384 57 · 0621 718 203 40</span>
      <span class="label">Fax</span><span>0621 384 57</span>
      <span class="label">E-Mail</span><span>praxis@brandt-oswald.de</span>
      <span class="label">Web</span><span>www.brandt-oswald.de</span>
    </div>
  </section>

  <section class="panel panel--hours">
    <svg class="accent" viewBox="0 0 600 388" aria-hidden="true">
      <polygon points="470,0 600,0 600,110" fill="var(--green)"/>
      <polygon points="540,0 600,0 600,50" fill="var(--green-dark)"/>
    </svg>
    <h2 class="hours-title">Öffnungszeiten</h2>
    <table class="hours">
      <tr><th>Mo, Di</th><td>08:00 – 12:00 Uhr &nbsp;·&nbsp; 14:00 – 16:00 Uhr</td></tr>
      <tr><th>Mi</th><td>08:00 – 12:00 Uhr</td></tr>
      <tr><th>Do, Fr</th><td>08:00 – 12:00 Uhr</td></tr>
    </table>
    <p class="notice"><strong>Wußten Sie schon?</strong><br>Sie können bei uns Termine über<br>www.terminofix.de vereinbaren.</p>
  </section>
</div>
</body>
</html>
```